Business Card Design Project

We require a business card template to cover basic contact information - our company logo, names of employees, title, mobile and email.

Target Market(s)

Corporate

Industry/Entity Type

Business

Font styles to use
Sans Serif

Requirements
Nice to have
• Thinking it would be great just to have the logo taking up approximately half the space (so it goes as far across the top of the card as possible) and then contact details in the lower half of the card. Keen just to use only the two colours in the logo, on a white background.
Should not have
• No fussy drawings

```html
<!DOCTYPE html>
<html lang="en">
<head>
<meta charset="utf-8">
<title>Fernvale developments – business cards</title>
<link rel="stylesheet" href="https://fonts.googleapis.com/css2?family=Jost:wght@300;400;500&display=swap">
<style>
  :root {
    --page: #e3eadb;
    --white: #ffffff;
    --teal: #45d5c0;
    --blue: #2a6fe6;
  }
  * { box-sizing: border-box; margin: 0; padding: 0; }
  html, body {
    width: 900px; height: 1200px; overflow: hidden;
    background: var(--page);
    font-family: "Jost", sans-serif;
  }
  .canvas { position: relative; width: 900px; height: 1200px; }

  .card { position: absolute; left: 90px; width: 720px; background: var(--white); }
  .card--split { top: 70px; height: 480px; }
  .card--stacked { top: 625px; height: 480px; }

  .brand {
    position: absolute; left: 0; right: 0; top: 0;
    color: var(--teal); font-weight: 500;
  }
  .brand__name {
    position: absolute; left: 16px; top: 6px;
    font-size: 182px; line-height: 1; letter-spacing: -4px;
  }
  .brand__tag {
    position: absolute; right: 20px;
    font-size: 40px; line-height: 1;
  }
  .card--split .brand__tag { top: 226px; }
  .card--stacked .brand__tag { top: 228px; }

  /* split layout */
  .split-band {
    position: absolute; left: 0; right: 0; top: 280px; bottom: 0;
    display: flex; gap: 2px; background: var(--white);
  }
  .split-band__col { background: var(--teal); position: relative; }
  .split-band__col--person { width: 292px; }
  .split-band__col--contact { flex: 1; }
  .person-name, .person-title {
    position: absolute; left: 14px; color: var(--white);
    font-size: 34px; font-weight: 500;
  }
  .card--split .person-name { top: 34px; }
  .card--split .person-title { top: 114px; }
  .contact-line {
    position: absolute; left: 6px; color: var(--blue);
    font-size: 35px; font-weight: 400; white-space: nowrap;
  }
  .contact-line--phone { top: 92px; }
  .contact-line--email { top: 150px; }

  /* stacked layout */
  .stack-name-row {
    position: absolute; left: 0; right: 0; top: 272px; height: 95px;
    background: var(--teal);
  }
  .stack-contact-row {
    position: absolute; left: 0; right: 0; top: 370px; bottom: 0;
    background: var(--teal);
  }
  .stack-name-row .person-name,
  .stack-name-row .person-title {
    color: var(--blue); top: 28px; font-size: 36px;
  }
  .stack-name-row .person-name { left: 8px; }
  .stack-name-row .person-title { left: 380px; }
  .stack-contact-row .contact-line {
    color: var(--white); font-weight: 300; font-size: 32px; left: 6px;
  }
  .stack-contact-row .contact-line--phone { top: 10px; }
  .stack-contact-row .contact-line--email { top: 68px; }
</style>
</head>
<body>
<main class="canvas">

  <section class="card card--split" aria-label="Business card, split layout">
    <div class="brand">
      <span class="brand__name">Fernvale</span>
      <span class="brand__tag">developments</span>
    </div>
    <div class="split-band">
      <div class="split-band__col split-band__col--person">
        <p class="person-name">Name</p>
        <p class="person-title">Title</p>
      </div>
      <div class="split-band__col split-band__col--contact">
        <p class="contact-line contact-line--phone">Phone: 484-555-0193</p>
        <p class="contact-line contact-line--email">eimail: fernvale@dev.com</p>
      </div>
    </div>
  </section>

  <section class="card card--stacked" aria-label="Business card, stacked layout">
    <div class="brand">
      <span class="brand__name">Fernvale</span>
      <span class="brand__tag">developments</span>
    </div>
    <div class="stack-name-row">
      <p class="person-name">Name</p>
      <p class="person-title">Title</p>
    </div>
    <div class="stack-contact-row">
      <p class="contact-line contact-line--phone">Mobile: 484-555-0193</p>
      <p class="contact-line contact-line--email">eimail: fernvale@dev.com</p>
    </div>
  </section>

</main>
</body>
</html>
```